Can you create a Business Card based on the Logo you designed.

See example and would like to see other examples.

Trying to keep it very clean with a focus on the logo and name.

```html
<!DOCTYPE html>
<html lang="en">
<head>
<meta charset="utf-8">
<title>Tillgro Business Card</title>
<link href="https://fonts.googleapis.com/css2?family=Montserrat:wght@400;500;700;800&display=swap" rel="stylesheet">
<style>
  :root {
    --backdrop: #e4e4e2;
    --card-white: #ffffff;
    --brand-green: #0f7449;
    --deep-green: #0a6b3c;
    --emboss-green: #0b5f3a;
    --accent-orange: #f39a2e;
    --text-grey: #555a57;
    --rule-green: #2f8a5c;
  }
  * { box-sizing: border-box; margin: 0; padding: 0; }
  html, body {
    width: 1200px; height: 801px; overflow: hidden;
    background: var(--backdrop);
    font-family: "Montserrat", sans-serif;
  }
  .canvas {
    width: 1200px; height: 801px;
    display: flex; align-items: center; justify-content: center; gap: 40px;
  }
  .card {
    width: 540px; height: 309px; border-radius: 18px;
    position: relative; overflow: hidden;
    box-shadow: 0 6px 18px rgba(0,0,0,0.12);
  }
  .card-front { background: var(--card-white); border: 1px solid #d9e8df; }
  .card-back { background: var(--brand-green); display: flex; align-items: center; justify-content: center; }

  .brand {
    display: flex; align-items: center; gap: 10px;
  }
  .brand-dot { width: 26px; height: 26px; border-radius: 50%; background: var(--accent-orange); }
  .brand-name { font-weight: 800; font-size: 52px; color: var(--deep-green); letter-spacing: -0.5px; line-height: 1; }

  .card-front .brand { position: absolute; left: 48px; top: 92px; }

  .divider {
    position: absolute; left: 318px; top: 112px; width: 1px; height: 62px; background: var(--rule-green);
  }
  .contact-list {
    position: absolute; left: 342px; top: 102px; list-style: none;
    display: flex; flex-direction: column; gap: 9px;
  }
  .contact-item {
    display: flex; align-items: center; gap: 9px;
    font-size: 14px; font-weight: 500; color: var(--text-grey);
  }
  .contact-icon { width: 12px; height: 12px; flex: none; }

  .holder { position: absolute; left: 48px; bottom: 46px; }
  .holder-name { font-weight: 700; font-size: 20px; color: var(--deep-green); }
  .holder-title { font-weight: 400; font-size: 14px; color: var(--text-grey); margin-top: 3px; }

  .card-back .brand-dot { background: var(--emboss-green); width: 34px; height: 34px; }
  .card-back .brand-name { color: var(--emboss-green); font-size: 70px; }
</style>
</head>
<body>
<main class="canvas">
  <section class="card card-front" aria-label="Business card front">
    <div class="brand">
      <span class="brand-dot"></span>
      <span class="brand-name">Tillgro</span>
    </div>
    <span class="divider"></span>
    <ul class="contact-list">
      <li class="contact-item">
        <svg class="contact-icon" viewBox="0 0 12 12"><path d="M2.5 1 L4.5 1 L5.2 3.5 L4 4.5 Q5 6.8 7.5 8 L8.5 6.8 L11 7.5 L11 9.5 Q10.5 11 9 11 Q1 10 1 2.5 Q1 1 2.5 1 Z" fill="#f39a2e"/></svg>
        +1 (555) 014-2298
      </li>
      <li class="contact-item">
        <svg class="contact-icon" viewBox="0 0 12 12"><rect x="0.5" y="2.5" width="11" height="7.5" rx="1" fill="#f39a2e"/><path d="M0.8 3 L6 7 L11.2 3" fill="none" stroke="#fff" stroke-width="1"/></svg>
        CEO@tillgro.com
      </li>
      <li class="contact-item">
        <svg class="contact-icon" viewBox="0 0 12 12"><circle cx="6" cy="6" r="5.5" fill="#f39a2e"/><path d="M0.5 6 H11.5 M6 0.5 Q3 6 6 11.5 M6 0.5 Q9 6 6 11.5" fill="none" stroke="#fff" stroke-width="0.8"/></svg>
        www.tillgro.com
      </li>
    </ul>
    <div class="holder">
      <p class="holder-name">Marcus Hale</p>
      <p class="holder-title">Chief Executive Officer</p>
    </div>
  </section>

  <section class="card card-back" aria-label="Business card back">
    <div class="brand">
      <span class="brand-dot"></span>
      <span class="brand-name">Tillgro</span>
    </div>
  </section>
</main>
</body>
</html>
```